Onboarding Infographic/brochure

We are a small criminal defense firm looking to create some sort of infographic or brochure that we can onboard new clients with. We are currently sending it out via email but want something a bit cooler and fun to send to clients. The information is:

A Few Quick Rules

We are here to help each step of the way. While questions are never discouraged, this letter will answer some of the most common ones we get asked.

Communications

As a client, you should always be in the loop. While we will try to respond to questions as quickly as possible, sometimes we are unable to respond right away. Do not worry - we promise to get back to you soon. Some questions might take some time to research, and a correct answer is better than a quick one.

Appointments

One of the benefits of having an attorney is the ability to discuss your case outside of court, minus the stress and headaches. If you need an appointment, please contact the office.

Appointments must be scheduled in advance. We do not want you to make a special trip to the office only to learn that we are in court or otherwise unavailable.

Jail Visits

If your family member is currently in jail, we take that very seriously. We will visit your loved one and introduce ourselves. While the case is ongoing, we ask that a family member be designated a “contact” person so that messages can be relayed quickly. Never discuss the facts of the case over the phone with someone who is in jail. Jail calls are recorded and we have seen too many cases go south based on remarks made over recorded lines.

Police Reports and Discovery

We will do our best to provide you with copies of everything we receive on your case. Most information will be emailed, so please keep your email address up to date.

Changes in Contact Information

If you move or change numbers during the case, please let us know. It is difficult to help if we are unable to reach you, and helping you is why we are here.

Court Appearances

Cases do not get resolved as quickly as they do on television. Expect there to be several hearings in your case and it may be necessary for you to attend one or more of them. If a hearing is set, you will receive notice of the date and time of each hearing.

Billing and Collections

We understand that this investment was a huge decision for you. As we focus on providing the best representation, we will need for you to stay on schedule with any payment arrangements agreed to at the time of your initial consultation.

Again, thank you for your trust in us. We look forward to getting a fantastic outcome on your case.

Target Market(s)

Criminal defense clients and their families

Industry/Entity Type

Legal

Font styles to use
Serif

Requirements
Must have
• Must incorporate all of the rules we email out. Would like diagrams, images or pictures
Nice to have
• We attached a Welcome brochure. Not sure I want it to look super similar, hence the request for infographic.

```html
<!DOCTYPE html>
<html lang="en">
<head>
<meta charset="utf-8">
<title>A Few Quick Rules – Client Onboarding</title>
<link href="https://fonts.googleapis.com/css2?family=Montserrat:wght@400;700&display=swap" rel="stylesheet">
<style>
  :root {
    --blue: #0a3cff;
    --panel: #d5dedc;
    --white: #ffffff;
    --ink: #1a1a1a;
    --dot: #c3cbca;
  }
  * { margin: 0; padding: 0; box-sizing: border-box; }
  html, body { width: 1200px; height: 980px; overflow: hidden; background: var(--white); }
  body { font-family: "Montserrat", Arial, sans-serif; color: var(--ink); position: relative; }

  .intro {
    position: absolute; left: 66px; top: 50px; width: 700px;
    font-weight: 700; font-size: 16.6px; line-height: 19px;
  }
  .brand {
    position: absolute; right: 66px; top: 58px;
    display: flex; align-items: center; gap: 10px;
    font-weight: 700; font-size: 21px; letter-spacing: 0.2px; color: var(--ink);
  }
  .brand-square { width: 14px; height: 14px; background: var(--blue); }

  .board { position: absolute; left: 0; top: 0; }

  .rule { position: absolute; }
  .rule h2 {
    color: var(--blue); font-weight: 700; font-size: 16.8px; line-height: 20px;
    margin-bottom: 21px;
  }
  .rule p { font-size: 13.4px; line-height: 16px; }
  .rule p + p { margin-top: 16px; }
  .rule.center { text-align: center; }
  .rule.right { text-align: right; }

  .hub-title {
    position: absolute; left: 500px; top: 522px; width: 200px; text-align: center;
    color: var(--blue); font-weight: 700; font-size: 16px; line-height: 19px;
  }

  .closing {
    position: absolute; left: 36px; top: 903px; width: 1128px; height: 41px;
    background: var(--blue); color: var(--white);
    display: flex; align-items: center; justify-content: center;
    font-weight: 700; font-size: 15.8px;
  }
</style>
</head>
<body>

<p class="intro">We are here to help each step of the way. While questions are never discouraged, this letter will answer some of the most common ones we get asked.</p>

<div class="brand"><span class="brand-square"></span>NORTHGATE DEFENSE PARTNERS</div>

<svg class="board" width="1200" height="980" viewBox="0 0 1200 980" aria-hidden="true">
  <rect x="36" y="129" width="1128" height="753" fill="var(--panel)"/>
  <g class="roads" fill="none" stroke="var(--white)" stroke-width="21" stroke-linejoin="round">
    <polyline points="600,120 600,400"/>
    <polyline points="30,355 336,355 497,440"/>
    <polyline points="1170,355 864,355 706,440"/>
    <polyline points="30,635 370,635 480,559"/>
    <polyline points="1170,635 830,635 723,559"/>
    <polyline points="353,890 536,627"/>
    <polyline points="847,890 666,627"/>
  </g>
  <g class="road-dots" fill="none" stroke="var(--dot)" stroke-width="4" stroke-linecap="round" stroke-dasharray="0 14.5">
    <polyline points="600,129 600,380"/>
    <polyline points="36,355 336,355 492,437"/>
    <polyline points="1164,355 864,355 711,437"/>
    <polyline points="36,635 370,635 478,560"/>
    <polyline points="1164,635 830,635 724,560"/>
    <polyline points="353,882 534,628"/>
    <polyline points="847,882 667,628"/>
  </g>
  <circle cx="600" cy="514" r="130" fill="var(--white)"/>
  <circle class="hub-ring" cx="600" cy="514" r="88" fill="none" stroke="var(--blue)" stroke-width="14"
          stroke-dasharray="70 9" transform="rotate(-87 600 514)"/>

  <g class="hub-book" fill="none" stroke="var(--blue)" stroke-width="2.2" stroke-linecap="round" stroke-linejoin="round">
    <rect x="570" y="469" width="28" height="45" rx="2"/>
    <rect x="602" y="469" width="28" height="45" rx="2"/>
    <path d="M568 474 v42 h64 v-42"/>
    <path d="M578 487 l4 4 l8 -8" stroke="#18b85a"/>
    <path d="M611 482 l8 8 m0 -8 l-8 8" stroke="#e8456b"/>
    <path d="M577 499 h14 M577 505 h14 M609 499 h14 M609 505 h14"/>
    <path d="M581 466 v9 l3 -2 l3 2 v-9" fill="var(--blue)"/>
  </g>

  <g class="badges" fill="var(--white)" stroke="var(--blue)" stroke-width="1.6">
    <circle cx="540" cy="399" r="21"/>
    <circle cx="660" cy="399" r="21"/>
    <circle cx="470" cy="499" r="21"/>
    <circle cx="730" cy="499" r="21"/>
    <circle cx="500" cy="600" r="21"/>
    <circle cx="700" cy="600" r="21"/>
    <circle cx="600" cy="646" r="21"/>
  </g>

  <g class="icons" fill="none" stroke="var(--blue)" stroke-width="1.5" stroke-linecap="round" stroke-linejoin="round">
    <!-- chat -->
    <path d="M527 390 h14 a3 3 0 0 1 3 3 v6 a3 3 0 0 1 -3 3 h-9 l-4 3 v-3 a3 3 0 0 1 -4 -3 v-6 a3 3 0 0 1 3 -3z"/>
    <path d="M540 398 h11 a3 3 0 0 1 3 3 v5 a3 3 0 0 1 -3 3 h-1 v3 l-4 -3 h-6 a3 3 0 0 1 -3 -3"/>
    <!-- calendar -->
    <rect x="648" y="388" width="20" height="20" rx="2"/>
    <path d="M648 393 h20 M653 386 v4 M663 386 v4 M652 398 h2 M657 398 h2 M652 403 h2"/>
    <circle cx="667" cy="406" r="5" fill="var(--white)"/><path d="M667 403.5 v2.5 l1.8 1.2"/>
    <!-- jail -->
    <rect x="460" y="488" width="20" height="22" rx="1"/>
    <path d="M465 488 v22 M470 488 v22 M475 488 v22 M460 498 h20"/>
    <!-- report -->
    <rect x="721" y="487" width="18" height="24" rx="1.5"/>
    <circle cx="730" cy="495" r="3.5"/><path d="M725 503 h10 M725 507 h10"/>
    <!-- id card -->
    <rect x="488" y="591" width="24" height="18" rx="2"/>
    <circle cx="494" cy="598" r="2.5"/><path d="M490 605 a4 4 0 0 1 8 0 M501 597 h8 M501 601 h8 M501 605 h8"/>
    <!-- bill -->
    <path d="M690 594 h14 v16 h-16 a2 2 0 0 1 -2 -2 v-3 h4z M694 599 h6 M694 603 h6"/>
    <circle cx="707" cy="593" r="6" fill="var(--white)"/>
    <path d="M709 591 h-3 a1.2 1.2 0 0 0 0 2.4 h2 a1.2 1.2 0 0 1 0 2.4 h-3 M707 589.5 v1.5 M707 595.8 v1.5"/>
    <!-- courthouse -->
    <path d="M589 641 l11 -6 l11 6z M590 643 h20 M593 645 v9 M598 645 v9 M602 645 v9 M607 645 v9 M588 656 h24"/>
  </g>
</svg>

<section class="rule" style="left:66px; top:158px; width:500px;">
  <h2>Communications</h2>
  <p>As a client, you should always be in the loop. While we will try to respond to questions as quickly as possible, sometimes we are unable to respond right away.</p>
  <p>Do not worry - we promise to get back to you soon. Some questions might take some time to research, and a correct answer is better than a quick one.</p>
</section>

<section class="rule" style="left:641px; top:158px; width:500px;">
  <h2>Appointments</h2>
  <p>One of the benefits of having an attorney is the ability to discuss your case outside of court, minus the stress and headaches. If you need an appointment, please contact the office.</p>
  <p>Appointments must be scheduled in advance. We do not want you to make a special trip to the office only to learn that we are in court or otherwise unavailable.</p>
</section>

<section class="rule" style="left:66px; top:393px; width:375px;">
  <h2>Jail Visits</h2>
  <p>If your family member is currently in jail, we take that very seriously. We will visit your loved one and introduce ourselves. While the case is ongoing, we ask that a family member be designated a “contact” person so that messages can be relayed quickly.</p>
  <p>Never discuss the facts of the case over the phone with someone who is in jail. Jail calls are recorded and we have seen too many cases go south based on remarks made over recorded lines.</p>
</section>

<section class="rule" style="left:792px; top:440px; width:352px;">
  <h2>Police Reports and Discovery</h2>
  <p>We will do our best to provide you with copies of everything we receive on your case. Most information will be emailed, so please keep your email address up to date.</p>
</section>

<section class="rule" style="left:66px; top:709px; width:322px;">
  <h2>Changes in Contact Information</h2>
  <p>If you move or change numbers during the case, please let us know. It is difficult to help if we are unable to reach you, and helping you is why we are here.</p>
</section>

<section class="rule center" style="left:436px; top:709px; width:328px;">
  <h2>Court Appearances</h2>
  <p>Cases do not get resolved as quickly as they do on television. Expect there to be several hearings in your case and it may be necessary for you to attend one or more of them. If a hearing is set, you will receive notice of the date and time of each hearing.</p>
</section>

<section class="rule right" style="left:800px; top:709px; width:334px;">
  <h2>Billing and Collections</h2>
  <p>We understand that this investment was a huge decision for you. As we focus on providing the best representation, we will need for you to stay on schedule with any payment arrangements agreed to at the time of your initial consultation.</p>
</section>

<div class="hub-title">A Few<br>Quick Rules</div>

<footer class="closing">Again, thank you for your trust in us. We look forward to getting a fantastic outcome on your case.</footer>

</body>
</html>
```